Beauty Salon Treatment Menu & Pricing

We need a Treatment Pricelist/ Brochure made to hand out to potential & existing customers! Meadowlark Body & Makeup is a small friendly beauty salon focused on the beauty essentials such as waxing, spray tanning, facials & makeup. We have a webpage with our colour theme and style and we would like to brochure to tie in.
www.meadowlarkbodyandmakeup.example.au.
We like a brochure that is clean, simple and easy to read.

Industry/Entity Type

Beauty Salon

```html
<!DOCTYPE html>
<html lang="en">
<head>
<meta charset="utf-8">
<title>Meadowlark Body &amp; Makeup – Treatment Menu</title>
<link href="https://fonts.googleapis.com/css2?family=Crimson+Text:wght@400;600;700&display=swap" rel="stylesheet">
<style>
  :root{
    --backdrop:#eeeae6;
    --pink-soft:#fbe3e7;
    --pink-mid:#f4c3cc;
    --heading-orange:#e8913a;
    --heading-pink:#cf4d74;
    --body-pink:#c06a85;
    --ink:#3a2a2e;
    --paper:#ffffff;
  }
  *{margin:0;padding:0;box-sizing:border-box}
  html,body{width:1200px;height:747px;overflow:hidden;background:var(--backdrop)}
  .spread{position:absolute;left:30px;top:13px;width:1140px;height:720px;display:flex;box-shadow:0 4px 14px rgba(0,0,0,.18)}
  .page{position:relative;width:570px;height:720px;overflow:hidden}

  /* cover page */
  .page--cover{background:linear-gradient(160deg,var(--pink-soft) 0%,#f8d4da 55%,var(--pink-mid) 100%)}
  .hero-photo{position:absolute;left:0;top:0;width:360px;height:720px;
    background:radial-gradient(ellipse at 45% 35%,#f6e6dc 0%,#efcfc2 35%,#e9b5b4 65%,rgba(244,195,204,0) 100%)}
  .brand{position:absolute;left:364px;top:52px;width:190px;font-family:"Crimson Text",serif;font-weight:600;color:var(--heading-pink);font-size:30px;line-height:32px}

  .pricelist{position:absolute;left:364px;top:150px;width:192px;font-family:"Crimson Text",serif;color:var(--ink);font-size:11.5px}
  .pricelist h2{font-size:11px;font-weight:700;color:var(--heading-orange);letter-spacing:.3px;margin:9px 0 2px;line-height:13px}
  .pricelist h2:first-child{margin-top:0}
  .row{display:flex;align-items:baseline;line-height:12.2px;white-space:nowrap}
  .row .leader{flex:1;border-bottom:1px dotted rgba(58,42,46,.55);margin:0 2px;transform:translateY(-3px)}

  /* menu page */
  .page--menu{background:linear-gradient(90deg,#e4e2e2 0%,var(--paper) 9%,var(--paper) 100%)}
  .menu-col{position:absolute;top:22px;font-family:"Crimson Text",serif;color:var(--body-pink);font-size:8.2px;line-height:1.22}
  .menu-col--left{left:33px;width:238px}
  .menu-col--right{left:290px;width:248px}
  .menu-col h3{font-size:13px;font-weight:700;color:var(--heading-pink);letter-spacing:.4px;margin:6px 0 2px}
  .menu-col h3:first-child{margin-top:0}
  .treatment{margin-bottom:9px}
  .treatment__head{display:flex;justify-content:space-between;color:var(--heading-pink);padding-right:30px}
  .line{display:flex;justify-content:space-between;padding-right:30px}
  .collage{position:absolute;left:0;top:0}
</style>
</head>
<body>
<div class="spread">
  <section class="page page--cover">
    <div class="hero-photo" role="img" aria-label="Photo of a smiling woman with a towel wrapped around her hair, touching her face"></div>
    <header class="brand">Meadowlark<br>Body &amp; Makeup</header>

    <div class="pricelist">
      <h2>FACIAL WAXING/ TINT</h2>
      <div class="row"><span>Eyebrow</span><span class="leader"></span><span>18.00</span></div>
      <div class="row"><span>Brow wax &amp; tint</span><span class="leader"></span><span>30.00</span></div>
      <div class="row"><span>Lip or chin or sides</span><span class="leader"></span><span>10.00</span></div>
      <div class="row"><span>Brow, lip &amp; chin</span><span class="leader"></span><span>33.00</span></div>
      <div class="row"><span>Full Face</span><span class="leader"></span><span>38.00</span></div>
      <div class="row"><span>Lash tint</span><span class="leader"></span><span>20.00</span></div>
      <div class="row"><span>Brow tint</span><span class="leader"></span><span>16.00</span></div>
      <div class="row"><span>Lash &amp; Brow tint</span><span class="leader"></span><span>30.00</span></div>

      <h2>MENS WAXING</h2>
      <div class="row"><span>Neck</span><span class="leader"></span><span>25.00</span></div>
      <div class="row"><span>Back (includes neck)</span><span class="leader"></span><span>40.00</span></div>
      <div class="row"><span>Chest</span><span class="leader"></span><span>35.00</span></div>
      <div class="row"><span>Chest &amp; Stomach</span><span class="leader"></span><span>40.00</span></div>
      <div class="row"><span>Back, Chest &amp; Stomach</span><span class="leader"></span><span>75.00</span></div>
      <div class="row"><span>Full Leg</span><span class="leader"></span><span>55.00</span></div>
      <div class="row"><span>Full Arm</span><span class="leader"></span><span>38.00</span></div>

      <h2>FEMALE WAXING</h2>
      <div class="row"><span>Brazilian</span><span class="leader"></span><span>45.00</span></div>
      <div class="row"><span>Extended Bikini</span><span class="leader"></span><span>30.00</span></div>
      <div class="row"><span>Basic Bikini</span><span class="leader"></span><span>18.00</span></div>
      <div class="row"><span>Full leg</span><span class="leader"></span><span>45.00</span></div>
      <div class="row"><span>Full Leg &amp; Basic Bikini</span><span class="leader"></span><span>50.00</span></div>
      <div class="row"><span>¾ Leg</span><span class="leader"></span><span>35.00</span></div>
      <div class="row"><span>¾ Leg &amp; Basic Bikini</span><span class="leader"></span><span>45.00</span></div>
      <div class="row"><span>Half Leg (inc knees)</span><span class="leader"></span><span>30.00</span></div>
      <div class="row"><span>Full Arm</span><span class="leader"></span><span>30.00</span></div>
      <div class="row"><span>Half Arm</span><span class="leader"></span><span>25.00</span></div>
      <div class="row"><span>Underarm</span><span class="leader"></span><span>18.00</span></div>
      <div class="row"><span>Stomach</span><span class="leader"></span><span>15.00</span></div>
      <div class="row"><span>Back</span><span class="leader"></span><span>20.00</span></div>
      <div class="row"><span>Patches, from</span><span class="leader"></span><span>10.00</span></div>
    </div>
  </section>

  <section class="page page--menu">
    <svg class="collage" width="570" height="720" viewBox="0 0 570 720" role="img" aria-label="Black and white photos of a makeup artist applying makeup to clients">
      <defs>
        <linearGradient id="greyTone" x1="0" y1="0" x2="1" y2="1">
          <stop offset="0" stop-color="#cfcfcf"/>
          <stop offset="0.5" stop-color="#9a9a9a"/>
          <stop offset="1" stop-color="#6e6e6e"/>
        </linearGradient>
      </defs>
      <path d="M0,720 L0,640 C120,600 200,640 270,600 C330,560 330,470 420,440 C480,420 540,430 570,420 L570,720 Z" fill="url(#greyTone)"/>
      <path d="M200,720 C260,640 330,600 420,580 C490,565 540,540 570,500" fill="none" stroke="#ffffff" stroke-width="10"/>
    </svg>

    <div class="menu-col menu-col--left">
      <h3>FACIALS</h3>
      <div class="treatment"><div class="treatment__head"><span>Quick Fix My Skin</span><span>65.00</span></div>
        Allow 30 minutes. A speedy refresh for busy days. Gentle cleansing, exfoliation, active serums and a soothing mask leave skin calm, bright and ready for the week.</div>
      <div class="treatment"><div class="treatment__head"><span>Glycolic Peel Treatment</span><span>55.00</span></div>
        Buy 4 and get the 5th treatment free (1 treatment p/w)<br>
        Allow 20 minutes. An active treatment that refines texture, evens tone and clears congestion. Ideal for dull skin, fine lines and uneven pigmentation, leaving a smooth fresh finish.</div>
      <div class="treatment"><div class="treatment__head"><span>Glycolic Microdermabrasion Treatment</span><span>100.00</span></div>
        Allow 45 minutes. A highly active treatment combining gentle microdermabrasion with a glycolic peel to lift away dead cells, reduce fine lines and boost radiance for a visibly fresher complexion.</div>
      <div class="treatment"><div class="treatment__head"><span>Clear Skin Facial</span><span>80.00</span></div>
        Allow 60 mins. A deep cleansing facial for oily, acne and congested skin types, using botanical extracts, clays and minerals to purify pores and calm redness.</div>
      <div class="treatment"><div class="treatment__head"><span>Rebalancing Vitamin A Facial</span><span>90.00</span></div>
        Allow 60 mins. A relaxing treatment for combination skin that refines, purifies and restores balance with vitamin rich serums, soothing plant extracts and a nourishing mask.</div>
      <div class="treatment"><div class="treatment__head"><span>Marine Radiance Facial</span><span>100.00</span></div>
        Allow 60 mins. A gentle hydrating treatment for every skin type, drawing on marine extracts, collagen and elastin to restore moisture and glow. Perfect before a special event.</div>
      <div class="treatment"><div class="treatment__head"><span>Anti Stress, Sensitive Skin Treatment</span><span>100.00</span></div>
        Allow 60 mins. Perfect for skin prone to redness, irritation and flaking. Calming botanicals and cool compresses soothe and protect, leaving skin comfortable and balanced.</div>
      <div class="treatment"><div class="treatment__head"><span>Anti Ageing Hydra Restore Facial</span><span>120.00</span></div>
        Allow 60 mins. A rich infusion of vitamins and oils for dehydrated, dry and tired skin. Leaves skin plump, supple and visibly smoother after one session.</div>
    </div>

    <div class="menu-col menu-col--right">
      <div class="treatment"><div class="treatment__head"><span>Firming Lift Facial</span><span>150.00</span></div>
        Allow 90 mins. Our most luxurious facial to firm, tone and lift. Peptide serums, a sculpting massage and a pearl eye treatment restore elasticity for mature or tired skin.</div>

      <h3>FACIAL ADD ONS</h3>
      <div>(Incorporate any of the following into a your<br>facial treatment for a small cost)</div>
      <div class="line"><span>Glycolic Peel</span><span>$20</span></div>
      <div class="line"><span>Firming Lift Caviar &amp; Pearl Eye Treatment</span><span>$20</span></div>
      <div class="line"><span>Firming Lift Neck &amp; Bust Treatment</span><span>$20</span></div>
      <div class="line"><span>Mini Pedicure (file &amp; Polish)</span><span>$10</span></div>

      <h3>TANNING</h3>
      <div class="line"><span>Spray Tan (every 10th tan free)</span><span>35.00</span></div>
      <div class="line"><span>Half Body Spray Tan</span><span>25.00</span></div>

      <h3>NAILS</h3>
      <div class="line"><span>Manicure</span><span>40.00</span></div>
      <div class="line"><span>Gel Colour Gloss Manicure</span><span>50.00</span></div>
      <div class="line"><span>Mini Manicure (file &amp; polish)</span><span>30.00</span></div>
      <div class="line"><span>Gel Polish Removal</span><span>15.00</span></div>

      <h3>MAKEUP</h3>
      <div class="line"><span>Bridal</span><span>95.00</span></div>
      <div>(we come to you, min 3 hour, includes lashes)</div>
      <div class="line"><span>Bridal Trial</span><span>100.00</span></div>
      <div>(includes take home lip colour)</div>
      <div class="line"><span>Special Occasion</span><span>100.00</span></div>
      <div class="line"><span>School Ball</span><span>70.00</span></div>
      <div class="line"><span>False Lash Application</span><span>25.00</span></div>
      <div>(includes lashes)</div>
    </div>
  </section>
</div>
</body>
</html>
```